Business cards for the RL Group

We are looking for a template for our new business cards for our company that we can edit ourselves.
You will find our company colors in the logo. the logo on the back and on the front
first name Last Name
position
E-mail address
mobile number
landline number
Companies we have 2 RL Sicherheit GmbH and RL Services GmbH
address
Lindenbergweg 42
22459 Hamburg
www.rlgruppe-nord.de

Something modern, simple but professional

if you have any questions, bring it on.

Sicherheit

Steht in der Beschreibung

F0912C
F2A743
F7CA91
FBE8D2
FDF5EE

• recognition value
• professional
• Playful

```html
<!DOCTYPE html>
<html lang="de">
<head>
<meta charset="utf-8">
<title>RL Gruppe – Visitenkarten</title>
<link rel="stylesheet" href="https://fonts.googleapis.com/css2?family=Roboto:wght@400;500;700&display=swap">
<style>
  :root {
    --bg: #c4c4c4;
    --card-light: #ffffff;
    --card-dark: #2b2b2b;
    --orange: #f0912c;
    --slate: #5d6a9a;
    --grey-text: #5a5a5a;
    --grey-mark: #6e6e6e;
    --light-text: #e9e9e9;
  }
  * { margin: 0; padding: 0; box-sizing: border-box; }
  html, body {
    width: 1200px; height: 900px; overflow: hidden;
    background: var(--bg);
    font-family: "Roboto", Arial, sans-serif;
  }
  .sheet {
    width: 1200px; height: 900px;
    display: flex; flex-direction: column;
    align-items: center; justify-content: center; gap: 44px;
  }
  .card {
    width: 630px; height: 360px;
    position: relative;
    box-shadow: 0 10px 26px rgba(0,0,0,0.22);
  }

  /* Front */
  .card-front { background: var(--card-light); }
  .holder { position: absolute; left: 46px; top: 42px; }
  .holder-name {
    color: var(--orange); font-weight: 700; font-size: 25px; letter-spacing: 0.5px;
  }
  .holder-role {
    color: var(--slate); font-size: 13px; letter-spacing: 1.6px; margin-top: 6px;
  }
  .divider {
    position: absolute; left: 46px; right: 46px; top: 160px;
    height: 1.5px; background: var(--orange);
  }
  .contact-list {
    position: absolute; left: 46px; top: 184px; list-style: none;
    color: var(--grey-text); font-size: 14px;
  }
  .contact-list li { display: flex; align-items: center; gap: 10px; margin-bottom: 8px; }
  .contact-list svg { width: 13px; height: 13px; flex: none; }
  .front-brand {
    position: absolute; right: 46px; top: 96px;
    display: flex; align-items: center; gap: 12px;
    background: var(--card-light); padding-left: 12px;
  }
  .address {
    position: absolute; right: 46px; bottom: 40px; text-align: right;
    color: var(--grey-text); font-size: 14px; line-height: 1.55;
  }

  /* Brand lockup */
  .brand-dot { border-radius: 50%; background: var(--orange); flex: none; }
  .brand-name { font-weight: 700; color: var(--grey-mark); letter-spacing: 1px; }
  .front-brand .brand-dot { width: 18px; height: 18px; }
  .front-brand .brand-name { font-size: 34px; }

  /* Back */
  .card-back {
    background: var(--card-dark);
    display: flex; flex-direction: column; align-items: center; justify-content: center; gap: 26px;
  }
  .back-brand { display: flex; align-items: center; gap: 18px; }
  .back-brand .brand-dot { width: 30px; height: 30px; }
  .back-brand .brand-name { font-size: 60px; }
  .companies { color: var(--light-text); font-size: 14px; letter-spacing: 0.4px; }
</style>
</head>
<body>
<main class="sheet">
  <section class="card card-front" aria-label="Visitenkarte Vorderseite">
    <div class="holder">
      <p class="holder-name">MAXIMILIAN REED</p>
      <p class="holder-role">DIRECTOR</p>
    </div>
    <div class="divider"></div>
    <div class="front-brand">
      <span class="brand-dot"></span>
      <span class="brand-name">RL GRUPPE</span>
    </div>
    <ul class="contact-list">
      <li>
        <svg viewBox="0 0 16 16" aria-hidden="true"><path fill="#f0912c" d="M3.5 1.5l2.5 3-1.5 1.7c.9 2 2.4 3.5 4.3 4.3L10.5 9l3 2.5-1.6 2.6C7 13.6 2.4 9 1.9 3.1z"/></svg>
        040 555 0192
      </li>
      <li>
        <svg viewBox="0 0 16 16" aria-hidden="true"><rect x="1" y="3" width="14" height="10" fill="#f0912c"/><path d="M1.5 3.5L8 9l6.5-5.5" stroke="#fff" stroke-width="1.3" fill="none"/></svg>
        kontakt@rlgruppe-nord.de
      </li>
      <li>
        <svg viewBox="0 0 16 16" aria-hidden="true"><circle cx="8" cy="8" r="6.5" fill="none" stroke="#f0912c" stroke-width="1.5"/><ellipse cx="8" cy="8" rx="2.8" ry="6.5" fill="none" stroke="#f0912c" stroke-width="1.2"/><path d="M1.5 8h13" stroke="#f0912c" stroke-width="1.2"/></svg>
        www.rlgruppe-nord.de
      </li>
    </ul>
    <address class="address" style="font-style:normal">
      Lindenbergweg 42<br>22459 Hamburg
    </address>
  </section>

  <section class="card card-back" aria-label="Visitenkarte Rückseite">
    <div class="back-brand">
      <span class="brand-dot"></span>
      <span class="brand-name">RL GRUPPE</span>
    </div>
    <p class="companies">RL Sicherheit GmbH | RL Services GmbH</p>
  </section>
</main>
</body>
</html>
```